Logo and Double sided business card

We need a logo and business card for a Point of Sale Business, Website is www.kestreltill.com.au - this is being worked on at the moment. There is a logo on the website - but this is more of a placement /logo and needs to be redesigned.
The address for Details for the Business card are

Person Name
KESTREL TILL
17/3 Worrigal Pde
Brindle Vale 2186
Ph 1300 585 926 (1300 KTL 926)
Email : Person@kestreltill.com.au
Web: www.kestreltill.com.au

Our company will be a Point of Sale installation and Support business. We Specialise in the Vandrel Quill system.

We do
Installation of POS Systems
Support and Maintenance of existing POS
Quill POS support
Updates

Target Market(s)

Restaurants, hotels, retail shops

Industry/Entity Type

Business

Contact Information for Business Card

Person Name
KESTREL TILL
17/3 Worrigal Pde
Brindle Vale 2186
Web: www.kestreltill.com.au

Logo Text

Kestrel Till

Font styles to use
Serif

Requirements
Must have
• We must have the source graphics in editable formats for both logo and business card.

```html
<!DOCTYPE html>
<html lang="en">
<head>
<meta charset="utf-8">
<title>Kestrel Till – Business Card</title>
<link rel="stylesheet" href="https://fonts.googleapis.com/css2?family=EB+Garamond:wght@400;500;600&display=swap">
<style>
  :root {
    --backdrop: #333031;
    --gold: #e8b92a;
    --paper: #f6f6f6;
    --ink: #6f6e72;
    --ring: #b6b5b8;
    --white: #ffffff;
  }
  * { margin: 0; padding: 0; box-sizing: border-box; }
  html, body {
    width: 1200px; height: 1000px; overflow: hidden;
    background: var(--backdrop);
    font-family: "EB Garamond", Garamond, "Times New Roman", serif;
  }
  .canvas { position: relative; width: 1200px; height: 1000px; }

  .card {
    position: absolute; left: 248px; width: 705px; height: 413px;
    overflow: hidden;
    box-shadow: 0 6px 18px rgba(0,0,0,0.35);
  }
  .card--front { top: 69px; background: var(--gold); }
  .card--back { top: 523px; background: var(--paper); }

  /* front */
  .front-ring {
    position: absolute; left: 268px; top: 88px;
    width: 170px; height: 170px; border-radius: 50%;
    border: 5px solid var(--white);
  }
  .front-name {
    position: absolute; left: 0; right: 0; top: 270px;
    text-align: center; color: var(--white);
    font-size: 50px; font-weight: 500; letter-spacing: 1px;
    line-height: 1.1;
  }

  /* back */
  .brand-ring {
    position: absolute; left: 32px; top: 37px;
    width: 68px; height: 68px; border-radius: 50%;
    border: 3px solid var(--ink);
  }
  .brand-name {
    position: absolute; left: 114px; top: 50px;
    color: var(--ink); font-size: 38px; font-weight: 400; letter-spacing: 0.5px;
    line-height: 1;
  }
  .holder {
    position: absolute; right: 30px; top: 44px; text-align: right; line-height: 1;
  }
  .holder__name { color: var(--ink); font-size: 32px; }
  .holder__role {
    color: var(--gold); font-size: 19px; font-weight: 600;
    letter-spacing: 1px; margin-top: 3px;
  }

  .contacts {
    position: absolute; left: 44px; top: 231px; list-style: none;
  }
  .contacts li {
    display: flex; align-items: center; height: 30px;
    color: var(--ink); font-size: 23px; font-weight: 500;
  }
  .contacts svg { width: 24px; height: 24px; margin-right: 12px; flex: none; }

  .address {
    position: absolute; left: 47px; top: 337px;
    color: var(--ink); font-size: 23px; font-weight: 500; line-height: 26px;
  }
  .address__company { font-weight: 600; }

  .deco-ring {
    position: absolute; left: 404px; top: 132px;
    width: 340px; height: 340px; border-radius: 50%;
    border: 10px solid var(--ring);
  }
</style>
</head>
<body>
<div class="canvas">

  <section class="card card--front" aria-label="Card front">
    <div class="front-ring"></div>
    <div class="front-name">KESTREL TILL</div>
  </section>

  <section class="card card--back" aria-label="Card back">
    <div class="deco-ring"></div>

    <div class="brand-ring"></div>
    <div class="brand-name">KESTREL TILL</div>

    <div class="holder">
      <div class="holder__name">Person Name</div>
      <div class="holder__role">MANAGER</div>
    </div>

    <ul class="contacts">
      <li>
        <svg viewBox="0 0 24 24" aria-hidden="true">
          <circle cx="12" cy="12" r="12" fill="var(--gold)"/>
          <path d="M7 10c0-2 2-3 5-3s5 1 5 3l-2 .5-1-1.5h-4l-1 1.5z" fill="#fff"/>
          <rect x="8" y="11" width="8" height="6" rx="1" fill="#fff"/>
          <circle cx="12" cy="14" r="1.5" fill="var(--gold)"/>
        </svg>
        1300 585 926 (1300 KTL 926)
      </li>
      <li>
        <svg viewBox="0 0 24 24" aria-hidden="true">
          <circle cx="12" cy="12" r="12" fill="var(--gold)"/>
          <rect x="6" y="8" width="12" height="8" fill="#fff"/>
          <path d="M6 8l6 5 6-5" fill="none" stroke="var(--gold)" stroke-width="1.2"/>
        </svg>
        Person@kestreltill.com.au
      </li>
      <li>
        <svg viewBox="0 0 24 24" aria-hidden="true">
          <circle cx="12" cy="12" r="12" fill="var(--gold)"/>
          <path d="M8 7h9v9l-3-3-4 4-3-3 4-4z" fill="#fff"/>
        </svg>
        www.kestreltill.com.au
      </li>
    </ul>

    <div class="address">
      <div class="address__company">KESTREL TILL</div>
      <div>17/3 Worrigal Pde, Brindle Vale 2186</div>
    </div>
  </section>

</div>
</body>
</html>
```